Brellin Trade Partners - we are Asian sourcing agents

We are sourcing agents based in the USA and we act as sourcing agents for clients in throughout the world. We focus primarily on custom sewn goods. So basically companies who do not have the in-house expertise to do it themselves, come to us and have us find suitable factories in Asia to do the production. We are middlemen. We find the factories...quote the project...manage the quality control and then deliver the goods directly to our customer's door. We pride ourselves in making the communication very easy and precise.

Current page is www.brellintrade.example

I am not happy w/ the overall look. The spacing...the photos, the fonts...the design elements...the pictures. I want a cool, crisp design that conveys professionalism and clearly depicts/explains what we do.

Requirements
Must have
• use my logo....I like it...it was designed by someone on this website.
Nice to have
• a video/animation of the entire process would be wonderful. Showing initial contact with our office in the USA...then to my correspondence with my offices in Taiwan and in Hong Kong...and then back and fort w/ the customer.....and then between my people in Hong Kong/Taiwan with the local factories......and then a quote is generated and sent to my client......to samples being made and sent for approval.....to a PO being generated......to final samples being sent.....to the order being shipped and delivered to the clients warehouse. I was thinking of an animation showing arrows and text showing the back and forth communication and explaining how the process flows.

```html
<!DOCTYPE html>
<html lang="en">
<head>
<meta charset="utf-8">
<title>Brellin Trade Partners</title>
<link href="https://fonts.googleapis.com/css2?family=Montserrat:wght@400;500;600;700;800&family=PT+Serif&display=swap" rel="stylesheet">
<style>
:root{
  --navy:#1b2a6b;
  --olive:#7a9a1e;
  --orange:#f05a28;
  --lime:#8cc63f;
  --yellow:#f6dc3a;
  --ink:#333;
  --soft-gray:#e2e3e5;
  --footer-bg:#8a887c;
  --link-blue:#2c86d1;
  --white:#fff;
}
*{margin:0;padding:0;box-sizing:border-box}
html,body{width:1200px;height:1190px;overflow:hidden;background:var(--footer-bg);font-family:"Montserrat",sans-serif}
.page{position:relative;width:1200px;height:1190px}
.header{position:absolute;left:0;top:0;width:1200px;height:176px;background:var(--white)}
.brand{position:absolute;left:110px;top:96px;font-size:29px;font-weight:800;color:var(--navy);letter-spacing:-.3px}
.brand-mark{display:inline-block;width:14px;height:14px;background:var(--olive);margin-right:10px;vertical-align:2px}
.nav{position:absolute;right:96px;top:113px;display:flex;gap:19px;font-size:15.5px;font-weight:500;letter-spacing:.6px;color:var(--navy)}
.nav .active{color:var(--olive)}
.hero{position:absolute;left:0;top:176px;width:1200px;height:400px;background:linear-gradient(115deg,#5e7a5a 0%,#7f9a72 35%,#6f8c68 60%,#4d6a55 100%)}
.hero-title{position:absolute;left:103px;top:108px;color:var(--white);font-weight:600;font-size:42px;line-height:1.1;text-shadow:0 2px 4px rgba(0,0,0,.45)}
.hero-title .big{display:block;font-size:34px;font-weight:700;letter-spacing:.5px}
.hero-sub{position:absolute;left:107px;top:210px;color:var(--white);font-size:21px;font-weight:600;line-height:1.05;text-shadow:0 2px 3px rgba(0,0,0,.45)}
.btn-quote{position:absolute;left:106px;top:271px;width:182px;height:48px;background:var(--orange);border-radius:6px;color:var(--white);font-weight:700;font-size:17px;letter-spacing:.8px;display:flex;align-items:center;justify-content:center}
.panel{position:absolute;left:58px;top:576px;width:1074px;height:517px;background:var(--white)}
.product{position:absolute;top:34px;width:226px;text-align:center}
.product-photo{height:146px;margin:0 auto;width:210px;border-radius:4px}
.product h3{margin-top:26px;font-size:17px;font-weight:600;color:var(--orange)}
.product p{margin-top:18px;font-size:11px;line-height:15.6px;color:var(--ink);font-weight:500}
.quote-box{position:absolute;left:815px;top:30px;width:235px;height:287px;background:var(--lime);color:var(--white);padding:16px 18px}
.quote-box h4{font-size:19px;font-weight:500;letter-spacing:.6px}
.quote-box .lead{margin-top:10px;font-size:14px;line-height:21.5px;padding-left:4px;font-weight:500}
.quote-box .contact{margin-top:14px;font-size:14px;line-height:21.5px;padding-left:10px;font-weight:500}
.btn-request{position:absolute;left:844px;top:281px;width:171px;height:50px;background:var(--yellow);border-radius:8px;color:#222;font-size:16.5px;font-weight:500;display:flex;align-items:center;justify-content:center}
.know{position:absolute;left:23px;top:364px;width:766px;height:112px;background:var(--soft-gray);text-align:center}
.know h5{margin-top:20px;font-family:"PT Serif",serif;font-weight:400;font-size:17px;color:var(--link-blue)}
.know-links{margin-top:12px;font-size:13.5px;color:#444;line-height:23.5px;text-align:left;padding-left:36px}
.know-links span{margin-right:22px}
.solutions{position:absolute;left:808px;top:364px;width:240px;height:119px;background:var(--yellow);border-radius:6px;text-align:center;padding-top:18px}
.solutions h5{font-size:17px;font-weight:500;letter-spacing:.5px;color:#222}
.solutions p{margin-top:6px;font-size:12.5px;line-height:20.5px;color:#222;font-weight:500}
.footer{position:absolute;left:102px;top:1114px;color:var(--white);font-family:Arial,sans-serif;font-size:12.5px;line-height:21px}
.social{position:absolute;right:64px;top:1125px;display:flex;gap:22px}
.social span{width:20px;height:20px;border-radius:50%;background:rgba(255,255,255,.8)}
</style>
</head>
<body>
<div class="page">
  <header class="header">
    <div class="brand"><span class="brand-mark"></span>Brellin Trade Partners</div>
    <nav class="nav">
      <span class="active">HOME</span><span>PRODUCT CATEGORIES</span><span>ABOUT US</span><span>REQUEST QUOTE</span>
    </nav>
  </header>

  <section class="hero" role="img" aria-label="Sewing thread spools, a blue tape measure and scissors on weathered green wood">
    <div class="hero-title">Asian Outsourcing<span class="big">MADE EASY!</span></div>
    <div class="hero-sub">Custom Sewn Goods Made<br>to Your Specifications</div>
    <div class="btn-quote">GET A QUOTE</div>
  </section>

  <main class="panel">
    <div class="product" style="left:39px">
      <div class="product-photo" role="img" aria-label="Black, grey and red messenger bag" style="background:linear-gradient(160deg,#555 0%,#333 45%,#b22 55%,#444 100%)"></div>
      <h3>Bags</h3>
      <p>Need to spread the word to customers? Try Public Relations, Press Releases, and Media Kits to help reporters get the facts...when you speak at events or interviews.</p>
    </div>
    <div class="product" style="left:292px">
      <div class="product-photo" role="img" aria-label="Row of colourful phone cases" style="background:linear-gradient(90deg,#222 0%,#2a3ab8 20%,#6a2bb0 40%,#c22aa8 55%,#d62020 75%,#e8a020 100%)"></div>
      <h3>Cases</h3>
      <p>Need help with social media? Want your own book on Shelfway? Let our creative marketing communication pros help you.. Go to Books &amp; Blogs.</p>
    </div>
    <div class="product" style="left:546px">
      <div class="product-photo" role="img" aria-label="Group of red, black and white golf bags" style="background:linear-gradient(90deg,#333 0%,#c33 25%,#eee 50%,#c33 75%,#333 100%)"></div>
      <h3>Sporting Goods</h3>
      <p>Do you treat your employees like an audience? They are! Our employee relations, employee career skills and talent development programs have helped businesses grow.</p>
    </div>

    <aside class="quote-box">
      <h4>REQUEST A QUOTE</h4>
      <p class="lead">Please contact us for immediate consultation regarding your outsourcing project.</p>
      <p class="contact">Tel: 555-210-4815<br>Fax: 555-210-4383<br>Email:<br>info@brellintrade.example</p>
    </aside>
    <div class="btn-request">Request Quote</div>

    <section class="know">
      <h5>WHAT YOU NEED TO KNOW</h5>
      <div class="know-links">
        <span>Contract Sewing in China</span><span>What is the Process?</span><span>What the Minimum Order?</span><br>
        <span>Contract Outsourcing FAQ</span><span>Outsourcing Case Study</span><span>Custom Industrial Sewing in China</span>
      </div>
    </section>

    <aside class="solutions">
      <h5>SOURCING SOLUTIONS</h5>
      <p>Bags&nbsp; Cases&nbsp; Covers&nbsp; Gloves<br>Medical&nbsp; Sewn Goods<br>Sporting Goods</p>
    </aside>
  </main>

  <footer class="footer">
    © 2015 Brellin<br>
    Home - Site Map – FAQ – Privacy Policy – Terms of Use – Contact Us
  </footer>
  <div class="social" aria-label="Social links"><span></span><span></span><span></span><span></span></div>
</div>
</body>
</html>
```